KTB Farriery

A letterhead that is fresh and eye catching plus that we where established 1914

Target Market(s)

Horse owners and collages

Requirements
Must have
• Fresh look eye catching
Looking modern
Nice to have
• A unique look

```html
<!DOCTYPE html>
<html lang="en">
<head>
<meta charset="utf-8">
<title>KTB Farriery Letterhead</title>
<link href="https://fonts.googleapis.com/css2?family=Montserrat:wght@300;400;500;600;700&family=Roboto+Slab:wght@400;700;800&family=Allura&display=swap" rel="stylesheet">
<style>
  :root{
    --bg:#e9eaec;
    --paper:#ffffff;
    --navy:#1c2a48;
    --gold:#c9a45f;
    --brown:#8a4a1c;
    --ink:#555a63;
    --muted:#8b9098;
    --grass-light:#7f9a3e;
    --grass-dark:#4d6a25;
    --accent:#f2b705;
  }
  *{margin:0;padding:0;box-sizing:border-box}
  html,body{width:1200px;height:1095px;overflow:hidden;background:var(--bg)}
  .letterhead{
    position:absolute;left:234px;top:30px;width:732px;height:1035px;
    background:var(--paper);box-shadow:0 4px 18px rgba(0,0,0,.12);
    overflow:hidden;font-family:'Montserrat',sans-serif;color:var(--ink);
  }
  .meadow{position:absolute;inset:0;width:732px;height:1035px}
  .sender{position:absolute;right:48px;top:48px;text-align:right}
  .sender-name{font-family:'Roboto Slab',serif;font-weight:800;font-size:26px;color:var(--navy);letter-spacing:1px}
  .sender-creds{font-family:'Roboto Slab',serif;font-weight:700;font-size:10px;color:var(--gold);margin-top:3px}
  .sender-role{font-family:'Roboto Slab',serif;font-size:11px;color:var(--navy);margin-top:2px}
  .brand{position:absolute;left:48px;top:145px;display:flex;align-items:center;gap:10px}
  .brand-dot{width:38px;height:38px;border-radius:50%;background:var(--navy)}
  .brand-text{display:flex;flex-direction:column}
  .brand-name{font-family:'Roboto Slab',serif;font-weight:800;font-size:20px;color:var(--navy);letter-spacing:1px;line-height:1.1}
  .brand-est{font-family:'Roboto Slab',serif;font-weight:700;font-size:10px;color:var(--gold);letter-spacing:2px;margin-top:3px}
  .date{position:absolute;right:48px;top:215px;font-size:10px;color:var(--muted)}
  .date b{color:var(--navy);font-weight:600}
  .recipient{position:absolute;left:48px;top:270px;font-size:9.5px;line-height:1.5;color:var(--muted);font-style:normal}
  .recipient-name{font-family:'Roboto Slab',serif;font-weight:700;font-size:14px;color:var(--navy)}
  .recipient-org{color:var(--navy);font-weight:500}
  .letter-body{position:absolute;left:48px;top:370px;width:560px;font-size:9.5px;line-height:1.65;font-weight:300}
  .salutation{font-weight:600;color:var(--navy);margin-bottom:14px;font-size:10px}
  .letter-body p{margin-bottom:14px}
  .signoff{position:absolute;left:48px;top:700px;width:200px}
  .signature{font-family:'Allura',cursive;font-size:40px;color:#2b2a6b;line-height:1;white-space:nowrap}
  .signoff-rule{border-top:1px solid #b9bcc2;margin-top:6px}
  .designation{font-size:9px;font-weight:600;letter-spacing:1px;color:var(--navy);margin-top:8px}
  .contact{position:absolute;left:48px;top:805px;font-family:'Roboto Slab',serif;font-size:11px;color:var(--navy);line-height:1.7}
  .contact b{color:var(--brown);font-weight:700}
</style>
</head>
<body>
<main class="letterhead">
  <svg class="meadow" viewBox="0 0 732 1035" role="img" aria-label="Photograph of horses grazing on a green meadow">
    <defs>
      <linearGradient id="grass" x1="0" y1="0" x2="0" y2="1">
        <stop offset="0" stop-color="var(--grass-light)"/>
        <stop offset="1" stop-color="var(--grass-dark)"/>
      </linearGradient>
    </defs>
    <path d="M732,730 C640,790 540,880 430,1035 L732,1035 Z" fill="url(#grass)"/>
    <line x1="730" y1="690" x2="730" y2="730" stroke="var(--accent)" stroke-width="4"/>
  </svg>

  <header class="sender">
    <div class="sender-name">DANIEL HARTLEY</div>
    <div class="sender-creds">D.W.C.F./ I.M.F.A./RF(Ire).RF(uk).EFFA.</div>
    <div class="sender-role">Master farrier at KTB farriers international</div>
  </header>

  <div class="brand">
    <span class="brand-dot"></span>
    <div class="brand-text">
      <span class="brand-name">KTB Farriery</span>
      <span class="brand-est">EST. 1914</span>
    </div>
  </div>

  <div class="date"><b>Date:</b> 07-06-2020</div>

  <address class="recipient">
    To<br>
    <span class="recipient-name">Samuel Green</span><br>
    <span class="recipient-org">CEO, Brightline Studio</span><br>
    4820 Elm Street NE Unit 12<br>
    Fairview, WA 98101
  </address>

  <section class="letter-body">
    <div class="salutation">Respected Sir,</div>
    <p>Vero primis his utin etiam oblique eosLorem ipsum dolor sit amet, quo dico choro ad. At eos euismod comprehe nsam. Assum malorum antiopam id vix, no vis suas essent possim. Ut vim utamur fierent, eum ne zril ridens el ectram. Nostrud atomorum ius id, cu deleniti placerat nec.Placerat deseruisse eum no, has ea eros atqui persecuti.</p>
    <p>Ei alia nihil cum. Ei putent disputando per, videveniam tacimates pro ut, dico rebum laboramus qui at. Congue fastidii consectetuer ut quo, vix nisl primain. Error tibique elaboraret nam ei, cu quodsi scripserit pro, oportere deseruisse conclusionemque ei mei. Eum aeterno scripta explicari ad, ad sit nonumy petentium.</p>
    <p>Ei reque liberavisse mei. Noster qualisque intellegam mea te, in eruditi erroribus voluptatibus eam. Pri omnis aperiam disputationi no. Pro ferri diceret pertinacia cu, tempor ancillae no vix. In justo atqui expetendis duo.Est nostro petentium te, esse clita debitis no vis, petentium gubergren vix ad. In tibique salutatus nam.</p>
    <p>Ne vis error ignota discere, nam in cetero consequat. Vis no summo tritani iudicabit, movet recteque philosophia sed ei, amet lobortis instructior cu est.Ut erat ipsum partiendo eam, eu vim quem quodsi lobortis, eam dico tincidunt no. Iuvaret placerat convenire qui ad. Vis hinc sensibus et, mei cu vidisse graecis.</p>
  </section>

  <div class="signoff">
    <div class="signature">Daniel Hartley</div>
    <div class="signoff-rule"></div>
    <div class="designation">DESIGNATION GOES HERE</div>
  </div>

  <footer class="contact">
    <div><b>P:</b> 01 5550 1234 00 <b>F:</b> 01 5550 1234 00 <b>E:</b> info@danielhartley.co.uk <b>W:</b> www.danielhartley.co.uk</div>
    <div>PO Box 2210, Oakfield House, Ashbury, Ireland</div>
  </footer>
</main>
</body>
</html>
```